High-end dermatology office brochure design

Corvellan Skin and Laser is a high-end dermatology practice that specializes in custom skin care solutions, and skin cancer surveillance and treatment. Brochure should be elegant, but informative to attract high-end customers.

Target Market(s)

Men and women 27-60

Industry/Entity Type

Office

Requirements
Must have
• Attached document has required copy, including, websites, address and company phone number
Nice to have
• images

```html
<!DOCTYPE html>
<html lang="en">
<head>
<meta charset="utf-8">
<title>Corvellan Skin and Laser – Brochure</title>
<link href="https://fonts.googleapis.com/css2?family=Great+Vibes&family=Roboto+Condensed:wght@400;700&family=Lato:wght@400;700&display=swap" rel="stylesheet">
<style>
  :root{
    --backdrop:#3a3a3c;
    --purple:#6a2c86;
    --purple-deep:#57206f;
    --purple-light:#9a55b0;
    --lavender:#b893c8;
    --lime:#c4dc2a;
    --gold:#e3d24a;
    --ink:#333333;
    --paper:#ffffff;
    --paper-shade:#e9e9ea;
  }
  *{box-sizing:border-box;margin:0;padding:0}
  html,body{width:1200px;height:907px;overflow:hidden}
  body{background:var(--backdrop);font-family:"Lato",sans-serif;color:var(--ink)}
  .spread{position:absolute;left:80px;top:88px;width:1040px;height:730px;display:flex}
  .page{position:relative;width:520px;height:730px;overflow:hidden;background:var(--paper)}
  .page--inside{background:linear-gradient(90deg,var(--paper-shade) 0%,var(--paper) 30%,var(--paper) 80%,#dcdcdd 100%)}
  .waves{position:absolute;left:0;top:0;width:520px;height:730px}

  /* Locations page */
  .locations-title{position:absolute;left:150px;top:70px;font-family:"Great Vibes",cursive;font-size:34px;color:var(--purple)}
  .locations-rule{position:absolute;left:140px;top:116px;width:190px;height:1px;background:var(--purple)}
  .location{position:absolute;width:170px;text-align:center}
  .location__city{font-family:"Roboto Condensed",sans-serif;font-weight:700;font-size:15px;color:var(--purple)}
  .location__map{width:92px;height:92px;border-radius:50%;margin:14px auto 16px;border:5px solid var(--purple);box-shadow:0 0 0 3px var(--lime) inset;background:radial-gradient(circle,#eeeeee,#d6d6d6)}
  .location__address{font-family:"Roboto Condensed",sans-serif;font-size:12.5px;line-height:1.3;color:var(--ink)}
  .location--phoenix{left:0;top:170px}
  .location--scottsdale{left:155px;top:140px}
  .location--honolulu{left:315px;top:120px}
  .coverage{position:absolute;left:40px;top:420px;width:440px;text-align:center;font-family:"Roboto Condensed",sans-serif;font-size:22px;line-height:1.3;color:var(--purple)}
  .brand-mark{position:absolute;font-family:"Roboto Condensed",sans-serif;font-weight:700;color:var(--purple);line-height:1.05}
  .brand-mark--back{left:300px;top:500px;font-size:22px;text-align:right;width:190px}
  .contact{position:absolute;font-size:13px;color:var(--paper);display:flex;align-items:center;gap:8px}
  .contact svg{flex:none}
  .contact--phone{left:60px;top:655px}
  .contact--web{left:60px;top:680px}
  .contact--shop{left:240px;top:650px}

  /* Cover page */
  .portrait{position:absolute;left:110px;top:0;width:410px;height:470px;background:radial-gradient(ellipse at 60% 45%,#f1d9cc 0%,#e7c4b3 40%,#f7f1ee 75%,#ffffff 100%)}
  .brand-mark--cover{left:30px;top:140px;font-size:20px}
  .cover-copy{position:absolute;left:20px;top:525px;width:490px;text-align:center;color:var(--paper)}
  .cover-copy__headline{font-family:"Roboto Condensed",sans-serif;font-size:30px;font-weight:400}
  .cover-copy__tagline{font-family:"Great Vibes",cursive;font-size:24px;color:var(--gold);margin-top:4px}
  .cover-copy__lead{font-family:"Lato",sans-serif;font-weight:700;font-size:14px;line-height:1.35;margin-top:6px}
  .cover-copy__body{font-size:7.5px;line-height:1.35;margin-top:10px}
</style>
</head>
<body>
<main class="spread">
  <section class="page page--inside">
    <svg class="waves" viewBox="0 0 520 730" aria-hidden="true">
      <path d="M0,525 C200,495 420,520 520,680 L520,730 L0,730 Z" fill="var(--paper)"/>
      <path d="M0,545 C200,515 420,545 510,690 L520,730 L0,730 Z" fill="var(--lime)"/>
      <path d="M0,585 C220,540 430,570 500,700 L520,730 L0,730 Z" fill="var(--paper)"/>
      <path d="M0,600 C230,560 440,590 495,710 L520,730 L0,730 Z" fill="var(--purple)"/>
    </svg>
    <h2 class="locations-title">Visit Our Location</h2>
    <div class="locations-rule"></div>

    <div class="location location--phoenix">
      <h3 class="location__city">Phoenix, Arizona</h3>
      <div class="location__map" role="img" aria-label="Street map of the Phoenix office"></div>
      <p class="location__address">Corvellan Skin &amp; Laser<br>2180 E Ridgeview Rd<br>Building #4<br>Suite #212<br>Phoenix, AZ 85048</p>
    </div>
    <div class="location location--scottsdale">
      <h3 class="location__city">Scottsdale, Arizona</h3>
      <div class="location__map" role="img" aria-label="Street map of the Scottsdale office"></div>
      <p class="location__address">Clearfield Skin Studio<br>Located in Wellhaven Center<br>7340 E Canyon Path<br>Suite #118<br>Scottsdale, AZ 85258</p>
    </div>
    <div class="location location--honolulu">
      <h3 class="location__city">Honolulu, Hawaii</h3>
      <div class="location__map" role="img" aria-label="Street map of the Honolulu office"></div>
      <p class="location__address">Pacific Skin Cancer Clinic<br>Two Harborview Tower<br>Suite #305<br>820 Kaimana St.<br>Honolulu, HI 96814</p>
    </div>

    <p class="coverage">We accept most major insurances and offer affordable self-pay rates.</p>
    <p class="brand-mark brand-mark--back">Corvellan<br>Skin and Laser</p>

    <p class="contact contact--phone">
      <svg width="11" height="11" viewBox="0 0 24 24"><path d="M6.6 10.8a15 15 0 0 0 6.6 6.6l2.2-2.2a1 1 0 0 1 1-.25 11 11 0 0 0 3.6.6 1 1 0 0 1 1 1V20a1 1 0 0 1-1 1A17 17 0 0 1 3 4a1 1 0 0 1 1-1h3.5a1 1 0 0 1 1 1 11 11 0 0 0 .6 3.6 1 1 0 0 1-.25 1z" fill="var(--lime)"/></svg>
      480-555-0172
    </p>
    <p class="contact contact--web">
      <svg width="9" height="9" viewBox="0 0 10 10"><circle cx="5" cy="5" r="5" fill="var(--lime)"/></svg>
      corvellanskincare.com
    </p>
    <p class="contact contact--shop">
      <svg width="9" height="9" viewBox="0 0 10 10"><circle cx="5" cy="5" r="5" fill="var(--lime)"/></svg>
      Shop at shopcorvellanskin.com
    </p>
  </section>

  <section class="page page--cover">
    <div class="portrait" role="img" aria-label="Close-up portrait photograph of a woman with clear skin"></div>
    <p class="brand-mark brand-mark--cover">Corvellan<br>Skin and Laser</p>
    <svg class="waves" viewBox="0 0 520 730" aria-hidden="true">
      <path d="M0,250 C30,400 160,470 520,440 L520,730 L0,730 Z" fill="var(--purple-light)"/>
      <path d="M0,330 C60,440 230,480 520,455 L520,730 L0,730 Z" fill="var(--lime)"/>
      <path d="M0,370 C80,470 260,500 520,470 L520,730 L0,730 Z" fill="var(--paper)"/>
      <path d="M0,385 C90,480 270,505 520,480 L520,730 L0,730 Z" fill="var(--lavender)"/>
      <path d="M0,420 C110,500 300,520 520,490 L520,730 L0,730 Z" fill="var(--paper)"/>
      <path d="M0,432 C120,510 310,530 520,500 L520,730 L0,730 Z" fill="var(--purple)"/>
    </svg>
    <div class="cover-copy">
      <h1 class="cover-copy__headline">A personalized approach to skin care</h1>
      <p class="cover-copy__tagline">Results you can see. Care you can feel</p>
      <p class="cover-copy__lead">Let us create a custom skin care regimen that best fits your medical and personal needs</p>
      <p class="cover-copy__body">We pride ourselves on providing premium skin care, to patients of all ages, with an honest and attentive approach. We're also proud to be leaders in skin cancer surveillance and specialize in the diagnosis and treatment of skin cancer.</p>
    </div>
  </section>
</main>
</body>
</html>
```